Real Estate 24"x24" Sign, Business Card, Letter Head and Envelope

This is a 4 project contest. If we choose a design or designs we like from what you sent we are willing to pay an amount at our discretion for that design even if we don't like all your designs for the 4 projects. Please be creative. Attached are our logo files. Please message us with any questions. Thanks and Good Luck!
Project 1: QLTV Realty 24" x 24" yard sign
We want to use the same blue background in our logo for the sign where the logo in white font will be on. CMYK 100,80,0,0. Attached is a sample a local designer made for you to get an idea what we are looking for. In the sample, the website is way too big and the entire sign is very plain and not attractive looking plus blue color is wrong one. We want the logo on top as large as possible but keeping it proportionate and attractive looking buy not too big that it looks odd. The following information can go in white color background or same blue color background color. Our company colors are blue (as per logo), green (as per logo), and white. "Residential & Commercial" goes under the logo. Under that put our phone number "312-948-6051" as large as possible but still looks good and under that our website in much smaller but readable font "www.qltvrealty.com".
Project 2: Envelope
We have two version of the logo. Use one or both. Whatever looks best in your design. The envelope will be white. We only want on top left corner logo and underneath our mailing address: 5197 Larchmere Ave. Skokie, IL 60093-1725. Maybe some creative decorative design at bottom of envelope will look nice
Project 3: Letter Head
We have two version of the logo. Use one or both. Whatever looks best in your design. We want the following information on the top of the letterhead. Logo, address: 5197 Larchmere Ave., Skokie, IL 60093-1725, phone: 312-948-6051, fax: 312-682-9307 website www.qltvrealty.com, email: info@qltvrealty.com
Project 4: Business card
Use either logo. We need cards for two individuals. Information for Person 1: Dev Kulkarni, Managing Broker, Phone: 312-948-6051, Email: dev.kulkarni@qltvrealty.com. Person 2: Ajay Kulkarni Broker Phone: 312-519-8263 Email: ajay.kulkarni@qltvrealty.com. Add Address, Fax and website same as above letter head.

```html
<!DOCTYPE html>
<html lang="en">
<head>
<meta charset="UTF-8">
<title>QLTV Realty Yard Sign</title>
<link rel="stylesheet" href="https://fonts.googleapis.com/css2?family=Montserrat:wght@500;600;700&display=swap">
<style>
  :root {
    --brand-blue: #0450a4;
    --ink-blue: #0b4f9f;
    --white: #ffffff;
    --divider-grey: #d3d3d3;
    --backdrop: #e8e8e8;
  }
  * { margin: 0; padding: 0; box-sizing: border-box; }
  html, body {
    width: 1200px;
    height: 1000px;
    overflow: hidden;
    background: var(--backdrop);
    font-family: "Montserrat", Arial, sans-serif;
  }
  .yard-sign {
    position: absolute;
    left: 186px;
    top: 86px;
    width: 828px;
    height: 828px;
    background: var(--white);
    overflow: hidden;
  }
  .sign-band {
    position: absolute;
    left: 0;
    top: 0;
    width: 828px;
    height: 828px;
  }
  .band-fill { fill: var(--brand-blue); }
  .band-edge { fill: var(--divider-grey); }
  .brand-name {
    position: absolute;
    left: 0;
    top: 200px;
    width: 100%;
    text-align: center;
    color: var(--white);
    font-weight: 700;
    font-size: 112px;
    letter-spacing: 2px;
    line-height: 1;
  }
  .sign-info {
    position: absolute;
    left: 0;
    top: 584px;
    width: 100%;
    text-align: center;
    color: var(--ink-blue);
  }
  .service-line {
    font-weight: 600;
    font-size: 41px;
    line-height: 1;
  }
  .phone-line {
    margin-top: 22px;
    display: flex;
    justify-content: center;
    align-items: center;
    gap: 16px;
  }
  .phone-icon { width: 72px; height: 72px; flex: none; }
  .phone-icon .tile { fill: var(--ink-blue); }
  .phone-icon .handset { fill: var(--white); }
  .phone-icon .wave { fill: none; stroke: var(--white); stroke-width: 2.5; stroke-linecap: round; }
  .phone-number {
    font-weight: 700;
    font-size: 86px;
    line-height: 1;
    letter-spacing: 1px;
  }
  .website {
    margin-top: 22px;
    font-weight: 600;
    font-size: 44px;
    line-height: 1;
  }
</style>
</head>
<body>
  <main class="yard-sign">
    <svg class="sign-band" viewBox="0 0 828 828" aria-hidden="true">
      <path class="band-edge" d="M0 498 Q414 640 828 498 V514 Q414 648 0 514 Z"/>
      <path class="band-fill" d="M0 0 H828 V498 Q414 638 0 498 Z"/>
    </svg>

    <h1 class="brand-name">QLTV Realty</h1>

    <section class="sign-info">
      <p class="service-line">Residential &amp; Commercial</p>
      <div class="phone-line">
        <svg class="phone-icon" viewBox="0 0 72 72" aria-hidden="true">
          <rect class="tile" x="0" y="0" width="72" height="72" rx="10"/>
          <path class="handset" d="M20 16 c3 -2 6 -1 7 2 l4 9 c1 2 0 4 -2 5 l-3 2 c2 6 7 11 13 13 l2 -3 c1 -2 3 -3 5 -2 l9 4 c3 1 4 4 2 7 l-3 4 c-3 3 -8 4 -13 2 c-13 -5 -22 -14 -27 -27 c-2 -5 -1 -10 2 -13 z"/>
          <path class="wave" d="M40 24 a10 10 0 0 1 9 9"/>
          <path class="wave" d="M40 17 a17 17 0 0 1 16 16"/>
          <path class="wave" d="M40 10 a24 24 0 0 1 23 23"/>
        </svg>
        <span class="phone-number">312-948-6051</span>
      </div>
      <p class="website">qltvrealty.com</p>
    </section>
  </main>
</body>
</html>
```